Brisa Vale residential and commercial cleaning

We need a Business card design for a new residential and commercial cleaning company based in UAE- Abu Dhabi named (BRISA VALE)
we provide a residential cleaning service based in hourly rate (Maid Rent - Baby Setting), Also a commercial and offices cleaning.
Our logo is attached for your reference

Target Market(s)

Women who are 22 to 60 years old.

Industry/Entity Type

Residential

Requirements
Should not have
• it should not have an old-style fonts

```html
<!DOCTYPE html>
<html lang="en">
<head>
<meta charset="utf-8">
<title>Brisa Vale – Business Card</title>
<link rel="stylesheet" href="https://fonts.googleapis.com/css2?family=Arimo:wght@400;700&family=Tinos&display=swap">
<style>
  :root {
    --stage: #9b9b9b;
    --card: #ffffff;
    --brand-blue: #1b6fc0;
    --band-blue: #0f5cb0;
    --mist-green: #e4f2d2;
    --mist-blue: #d3e4f4;
    --ink: #2b2b2b;
    --label: #333333;
  }
  * { box-sizing: border-box; margin: 0; padding: 0; }
  html, body { width: 1200px; height: 885px; overflow: hidden; }
  body { background: var(--stage); font-family: "Arimo", Arial, sans-serif; position: relative; }

  .card { position: absolute; background: var(--card); }
  .card--front { left: 88px; top: 88px; width: 593px; height: 361px; }
  .card--back  { left: 537px; top: 384px; width: 590px; height: 361px; overflow: hidden; }

  .side-label { position: absolute; font-size: 50px; color: var(--label); line-height: 1; }
  .side-label--front { left: 173px; top: 448px; }
  .side-label--back  { left: 741px; top: 768px; }

  .wordmark {
    position: absolute; font-weight: 700; color: var(--brand-blue);
    white-space: nowrap; line-height: 1;
  }
  .wordmark--front {
    left: 0; right: 0; top: 150px; text-align: center; font-size: 64px;
  }
  .wordmark--back { right: 37px; top: 288px; font-size: 28px; }

  .top-rule { position: absolute; left: 0; top: 10px; width: 590px; height: 3px; background: var(--band-blue); }
  .contact-band {
    position: absolute; left: 0; top: 19px; width: 590px; height: 33px;
    background: var(--band-blue); color: #fff; font-size: 19px;
    display: flex; justify-content: space-between; align-items: center;
    padding: 0 37px 0 40px;
  }

  .brand-backdrop {
    position: absolute; left: 0; top: 52px; width: 234px; height: 182px;
    background: linear-gradient(160deg, var(--mist-blue) 0%, var(--mist-green) 60%, rgba(255,255,255,0) 100%);
  }

  .identity { position: absolute; right: 37px; top: 96px; text-align: right; }
  .identity__name { font-family: "Tinos", "Times New Roman", serif; font-size: 35px; color: var(--ink); line-height: 1.1; }
  .identity__role { font-size: 19px; color: var(--ink); margin-top: 6px; }
  .identity__phone { font-size: 18px; color: var(--ink); margin-top: 6px; letter-spacing: 0.5px; }

  .office-details {
    position: absolute; left: 38px; top: 275px; list-style: none;
    font-family: "Tinos", "Times New Roman", serif; font-size: 17px; color: var(--ink); line-height: 21px;
  }
  .office-details li::before { content: "• "; }
</style>
</head>
<body>
  <section class="card card--front" aria-label="Card front">
    <p class="wordmark wordmark--front">Brisa Vale</p>
  </section>
  <p class="side-label side-label--front">Front</p>

  <section class="card card--back" aria-label="Card back">
    <div class="top-rule"></div>
    <div class="contact-band"><span>hello@brisavale.com</span><span>www.website.com</span></div>
    <div class="brand-backdrop" role="img" aria-label="Faint brand emblem backdrop"></div>
    <div class="identity">
      <p class="identity__name">YOUR NAME</p>
      <p class="identity__role">Designation</p>
      <p class="identity__phone">XXX XXX XXX XXX</p>
    </div>
    <ul class="office-details">
      <li>Office Address Line</li>
      <li>P + 222 2222</li>
      <li>F + 222 2222</li>
    </ul>
    <p class="wordmark wordmark--back">Brisa Vale</p>
  </section>
  <p class="side-label side-label--back">Back</p>
</body>
</html>
```